Coffee Roaster Needs A Postcard Design

I am coffee roaster ( a home business) and I would like to create a neighborhood delivery service. Once a month I would delivery fresh roasted coffee to my neighbors. I would like to create a postcard to advertise the coffee delivery service.

Preferences: The postcard would be very simple, primarily black and white ( a little color) with visuals; fresh roasted coffee beans, delivered to the doorstep, a great cup of coffee. Simple steps, 1 2 & 3.

I have a website the postcard advertisement should flow with the site : www.brambledgebeanworks.com

Target Market(s)

Upper class residential neighborhood

Industry/Entity Type

Business

Font styles to use
Serif

Colors
f04a50

Requirements
Must have
• Images _ Coffee Beans

```html
<!DOCTYPE html>
<html lang="en">
<head>
<meta charset="utf-8">
<title>Brambledge Beanworks – Postcard</title>
<link rel="stylesheet" href="https://fonts.googleapis.com/css2?family=Josefin+Sans:wght@400;600&family=Lato:wght@400;700&family=Oswald:wght@300;400&display=swap">
<style>
  :root {
    --stage: #ece8e2;
    --espresso: #2a1714;
    --espresso-deep: #1e100e;
    --bean-brown: #4a2a1c;
    --bar-brown: #55311f;
    --gold: #c9bf7a;
    --gold-line: #8c7440;
    --cream: #ffffff;
    --mist: #d9d6d8;
    --plum: #3a2230;
    --moss: #5d6f5e;
    --mint: #8fb3a2;
    --tan: #c6a789;
    --tan-dark: #7a5a44;
    --kraft: #b89878;
    --ink: #2b1a14;
  }
  * { margin: 0; padding: 0; box-sizing: border-box; }
  html, body { width: 1200px; height: 554px; overflow: hidden; background: var(--stage); }
  .canvas { position: relative; width: 1200px; height: 554px; }

  /* Front card */
  .card { position: absolute; overflow: hidden; box-shadow: 0 2px 6px rgba(0,0,0,.25); }
  .card-front { left: 60px; top: 78px; width: 515px; height: 398px;
    background: linear-gradient(to bottom, var(--espresso) 0, var(--espresso) 83px, var(--espresso-deep) 84px, #3a2a2b 170px, #8d8788 240px, var(--mist) 270px, #f2f1f1 300px); }
  .front-header { position: absolute; left: 0; top: 0; width: 100%; height: 82px; border-bottom: 3px solid var(--gold-line); }
  .delivers-title { position: absolute; left: 38px; top: 15px; font: 400 16px 'Lato', sans-serif; color: var(--gold); }
  .delivers-sub { position: absolute; left: 38px; top: 43px; font: 400 11.5px/15px 'Lato', sans-serif; color: var(--gold); letter-spacing: .3px; }
  .brand-stack { position: absolute; right: 28px; top: 12px; font: 400 20px/21px 'Josefin Sans', sans-serif; color: var(--cream); letter-spacing: 3.2px; text-align: left; }
  .steps { position: absolute; left: 40px; top: 97px; list-style: none; }
  .steps li { display: flex; align-items: center; gap: 8px; font: 700 13.5px/23px 'Lato', sans-serif; color: var(--cream); }
  .steps svg { width: 14px; height: 14px; fill: none; stroke: var(--cream); stroke-width: 1.6; }
  .goals { position: absolute; left: 358px; top: 98px; width: 130px; text-align: center; color: var(--cream); }
  .goals h3 { font: 400 12px 'Lato', sans-serif; letter-spacing: .5px; margin-bottom: 6px; }
  .goals p { font: 400 9px/11px 'Lato', sans-serif; }
  .tagline { position: absolute; left: 0; width: 100%; top: 224px; text-align: center; font: 400 16px 'Josefin Sans', sans-serif; letter-spacing: 3px; color: var(--gold); }
  .beans-photo { position: absolute; left: 0; bottom: 0; width: 100%; height: 140px;
    background: linear-gradient(to bottom, rgba(90,55,35,0) 0, #6a4128 28px, var(--bean-brown) 60px, #3b2216 100%); }
  .web-bar { position: absolute; left: 0; top: 326px; width: 100%; height: 28px; background: var(--bar-brown);
    font: 700 14.5px/28px 'Lato', sans-serif; color: var(--cream); text-align: right; padding-right: 22px; }

  /* Back card */
  .card-back { left: 632px; top: 82px; width: 515px; height: 394px; background: var(--tan); }
  .scooter-photo { position: absolute; left: 0; top: 0; width: 248px; height: 100%;
    background: linear-gradient(160deg, var(--plum) 0%, #2c2a26 40%, var(--moss) 70%, var(--mint) 100%); }
  .back-brand { position: absolute; left: 22px; top: 17px; font: 400 18.5px/20px 'Josefin Sans', sans-serif; letter-spacing: 3px; color: var(--cream); }
  .back-sub { position: absolute; left: 24px; top: 84px; font: 400 11px 'Oswald', sans-serif; letter-spacing: 1.3px; color: #b9aeb0; }
  .order-panel { position: absolute; left: 248px; top: 0; width: 267px; height: 198px; background: linear-gradient(to right, #cfb49a, var(--tan)); }
  .order-head { position: absolute; left: 8px; top: 10px; font: 300 15.5px/18px 'Oswald', sans-serif; color: var(--ink); letter-spacing: .6px; }
  .contact-band { position: absolute; left: 0; top: 62px; width: 100%; height: 52px; background: rgba(110,80,60,.55);
    padding: 6px 0 0 10px; color: var(--cream); }
  .contact-band .web { font: 700 11px/14px 'Lato', sans-serif; letter-spacing: .4px; }
  .contact-band .phone { display: flex; align-items: center; gap: 3px; font: 700 14px/16px 'Lato', sans-serif; }
  .contact-band .phone svg { width: 12px; height: 12px; fill: var(--cream); }
  .contact-band .mail { font: 400 9.5px/13px 'Lato', sans-serif; }
  .about { position: absolute; left: 20px; top: 128px; width: 238px; font: 400 9.5px/11.5px 'Lato', sans-serif; color: var(--ink); }
  .bags-photo { position: absolute; left: 248px; top: 198px; width: 267px; height: 196px;
    background: linear-gradient(to bottom, #d6cfc6 0%, var(--kraft) 30%, #a78665 70%, var(--tan-dark) 100%); }
</style>
</head>
<body>
<main class="canvas">

  <section class="card card-front">
    <header class="front-header">
      <h2 class="delivers-title">Brambledge Beanworks Delivers</h2>
      <p class="delivers-sub">COFFEE AT YOUR DOORSTEP<br>WEEKLY | SEMI-MONTHLY | MONTHLY</p>
      <div class="brand-stack">BRAMBLEDGE<br>BEANWORKS</div>
    </header>

    <ul class="steps">
      <li><svg viewBox="0 0 16 16"><circle cx="8" cy="8" r="6.5"/><ellipse cx="8" cy="8" rx="3" ry="6.5"/><path d="M1.5 8h13M2.5 4.8h11M2.5 11.2h11"/></svg>We source first class beans</li>
      <li><svg viewBox="0 0 16 16" style="fill:#fff;stroke:none"><path d="M8 14.5 1.8 8.4A3.7 3.7 0 0 1 8 3.6a3.7 3.7 0 0 1 6.2 4.8z"/></svg>We carefully roast them</li>
      <li><svg viewBox="0 0 16 16" style="fill:#fff;stroke:none"><path d="M1 3.5h14v9H1z"/><path d="M1 3.5 8 9l7-5.5" fill="none" stroke="#2a1714" stroke-width="1.2"/></svg>We deliver right to your door</li>
    </ul>

    <div class="goals">
      <h3>GOALS</h3>
      <p>Our goal is to make delicious, fresh roasted coffee available to everyone who loves coffee as much as we do.</p>
    </div>

    <p class="tagline">MORE BEANS, LESS HASSLE</p>

    <div class="beans-photo" role="img" aria-label="Scattered roasted coffee beans"></div>
    <div class="web-bar">www.brambledgebeanworks.com</div>
  </section>

  <section class="card card-back">
    <div class="scooter-photo" role="img" aria-label="Stylised mint scooter front parked outdoors"></div>
    <div class="back-brand">BRAMBLEDGE<br>BEANWORKS</div>
    <p class="back-sub">COFFEE BEAN SUBSCRIPTION</p>

    <div class="order-panel">
      <h2 class="order-head">ORDER YOUR FIRST BAG OF<br>BRAMBLEDGE BEANWORKS AT:</h2>
      <div class="contact-band">
        <div class="web">www.brambledgebeanworks.com</div>
        <div class="phone"><svg viewBox="0 0 16 16"><path d="M4 1.5 6.3 4 5 6a9 9 0 0 0 5 5l2-1.3 2.5 2.3-1.6 2.2C7.5 14 2 8.5 1.8 3.1z"/></svg>707.555.0148</div>
        <div class="mail">BRAMBLEDGEBEANWORKS@MAIL.COM</div>
      </div>
      <p class="about">We specialize in small batch coffee roasting using responsibly sourced beans from Guatemala, Kenya, Bolivia and beyond. We are a true family business — the result of Southern charm meets West Coast inspiration.</p>
    </div>

    <div class="bags-photo" role="img" aria-label="Row of kraft paper coffee bags with white labels"></div>
  </section>

</main>
</body>
</html>
```